Vantrell OBGYN Partners LLC
...connect the dots (docs!)
Vantrell OBGYN Partners LLC -
Creative Brief
Simple
Dr. Marlene Fostwick-Abara MD FACOG
2846 Quillan Avenue Suite 240 Tucker, Ga 30091
marlene@vantrellobgynpartners.example
www.vantrellobgynpartners.example
Desire same logo continued with above second line listed as in Hire-a-medic logo by KARBIMOSS design#12 with above adjustment in subtitle
Vantrell OBGYN Partners Locum tenens option for OBGYN's ...connect to us and we will help you connect the dots in your day!

```html
<!DOCTYPE html>
<html lang="en">
<head>
<meta charset="utf-8">
<title>Vantrell OBGYN Partners LLC — Stationery Set</title>
<link href="https://fonts.googleapis.com/css2?family=Questrial&display=swap" rel="stylesheet">
<style>
  :root{
    --backdrop:#2f2f31;
    --paper:#ffffff;
    --paper-shade:#f1f1f2;
    --teal:#2fb7c6;
    --pink:#e0197f;
    --ink:#5b5b60;
    --ink-soft:#9a9aa0;
  }
  *{margin:0;padding:0;box-sizing:border-box}
  html,body{width:1200px;height:845px;overflow:hidden}
  body{background:var(--backdrop);font-family:"Questrial",sans-serif;position:relative;color:var(--ink)}
  .sheet{position:absolute;background:var(--paper);overflow:hidden;box-shadow:0 3px 10px rgba(0,0,0,.45)}
  .brand{display:flex;align-items:center;gap:5px;color:var(--teal);white-space:nowrap}
  .brand-dot{width:7px;height:7px;border-radius:50%;background:var(--pink);flex:none}
  .tagline{color:var(--ink-soft);font-size:6px;margin-top:2px}
  .contact{font-size:5px;line-height:1.55;color:var(--ink-soft)}
  .band-pink{position:absolute;left:0;right:0;bottom:0;background:var(--pink)}
  .band-teal{position:absolute;left:0;right:0;bottom:0;background:var(--teal)}

  /* letterhead */
  .letterhead{left:137px;top:271px;width:290px;height:406px}
  .letterhead .masthead{position:absolute;left:34px;top:30px;font-size:10px}
  .letterhead .footer-address{position:absolute;left:0;right:0;bottom:18px;text-align:center;font-size:4.5px;color:var(--ink-soft)}
  .letterhead .band-pink{height:12px;display:flex;align-items:center;justify-content:center;color:#fff;font-size:4.5px}

  /* business cards */
  .card{width:150px;height:91px;top:283px}
  .card-front-a{left:456px}
  .card-front-b{left:617px}
  .card .masthead{position:absolute;left:10px;top:14px;font-size:6px}
  .card .masthead .tagline{font-size:4px}
  .card .contact{position:absolute;left:10px;top:38px;font-size:4px}
  .card-front-a .band-teal,.card-front-b .band-pink{height:5px}
  .card-solid{display:flex;flex-direction:column;align-items:center;justify-content:center;text-align:center}
  .card-teal{left:782px;background:var(--teal)}
  .card-pink{left:941px;background:var(--pink)}
  .card-solid .brand{color:#fff;font-size:7px}
  .card-solid .brand-dot{background:#fff}
  .card-solid .tagline{color:rgba(255,255,255,.85);font-size:4.5px}

  /* envelopes */
  .envelope-front{left:456px;top:389px;width:312px;height:134px}
  .envelope-back{left:456px;top:538px;width:312px;height:120px;background:var(--paper-shade)}
  .envelope-front .masthead{position:absolute;left:16px;top:16px;font-size:8px}
  .envelope-front .contact{position:absolute;left:16px;top:46px}
  .envelope-front .band-pink{height:10px}
  .envelope-back .flap{position:absolute;inset:0}
  .envelope-back .masthead{position:absolute;left:0;right:0;top:8px;display:flex;flex-direction:column;align-items:center;font-size:6px}
  .envelope-back .contact{position:absolute;left:0;right:0;bottom:12px;text-align:center}
  .envelope-back .band-pink{height:6px}

  .envelope-color{width:310px}
  .envelope-teal{left:782px;top:389px;height:134px;background:var(--teal)}
  .envelope-pink{left:782px;top:538px;height:139px;background:var(--pink)}
  .envelope-color .masthead{position:absolute;left:16px;bottom:34px;font-size:8px}
  .envelope-color .brand{color:#fff}
  .envelope-color .brand-dot{background:#fff}
  .envelope-color .tagline{color:rgba(255,255,255,.85)}
  .envelope-color .contact{position:absolute;left:16px;bottom:10px;color:rgba(255,255,255,.9)}
</style>
</head>
<body>

<section class="sheet letterhead" aria-label="Letterhead">
  <div class="masthead">
    <div class="brand"><span class="brand-dot"></span>Vantrell OBGYN Partners LLC</div>
    <div class="tagline">...connect the dots (docs!)</div>
  </div>
  <p class="footer-address">2846 Quillan Avenue Suite 240 Tucker, Ga 30091 · marlene@vantrellobgynpartners.example</p>
  <div class="band-pink">www.vantrellobgynpartners.example</div>
</section>

<section class="sheet card card-front-a" aria-label="Business card front">
  <div class="masthead">
    <div class="brand"><span class="brand-dot"></span>Vantrell OBGYN Partners LLC</div>
    <div class="tagline">...connect the dots (docs!)</div>
  </div>
  <div class="contact">
    Dr. Marlene Fostwick-Abara MD FACOG<br>
    2846 Quillan Avenue Suite 240<br>
    Tucker, Ga 30091<br>
    marlene@vantrellobgynpartners.example<br>
    www.vantrellobgynpartners.example
  </div>
  <div class="band-teal"></div>
</section>

<section class="sheet card card-front-b" aria-label="Business card front, pink variant">
  <div class="masthead">
    <div class="brand"><span class="brand-dot"></span>Vantrell OBGYN Partners LLC</div>
    <div class="tagline">...connect the dots (docs!)</div>
  </div>
  <div class="contact">
    Dr. Marlene Fostwick-Abara MD FACOG<br>
    2846 Quillan Avenue Suite 240<br>
    Tucker, Ga 30091<br>
    marlene@vantrellobgynpartners.example<br>
    www.vantrellobgynpartners.example
  </div>
  <div class="band-pink"></div>
</section>

<section class="sheet card card-solid card-teal" aria-label="Business card back, teal">
  <div class="brand"><span class="brand-dot"></span>Vantrell OBGYN Partners LLC</div>
  <div class="tagline">...connect the dots (docs!)</div>
</section>

<section class="sheet card card-solid card-pink" aria-label="Business card back, pink">
  <div class="brand"><span class="brand-dot"></span>Vantrell OBGYN Partners LLC</div>
  <div class="tagline">...connect the dots (docs!)</div>
</section>

<section class="sheet envelope-front" aria-label="Envelope front">
  <div class="masthead">
    <div class="brand"><span class="brand-dot"></span>Vantrell OBGYN Partners LLC</div>
    <div class="tagline">...connect the dots (docs!)</div>
  </div>
  <div class="contact">2846 Quillan Avenue Suite 240<br>Tucker, Ga 30091</div>
  <div class="band-pink"></div>
</section>

<section class="sheet envelope-back" aria-label="Envelope back">
  <svg class="flap" width="312" height="120" viewBox="0 0 312 120">
    <path d="M0 0 L156 62 L312 0" fill="#fff" stroke="#dcdce0" stroke-width="1"/>
  </svg>
  <div class="masthead">
    <div class="brand"><span class="brand-dot"></span>Vantrell OBGYN Partners LLC</div>
    <div class="tagline">...connect the dots (docs!)</div>
  </div>
  <div class="contact">www.vantrellobgynpartners.example</div>
  <div class="band-pink"></div>
</section>

<section class="sheet envelope-color envelope-teal" aria-label="Envelope, teal">
  <div class="masthead">
    <div class="brand"><span class="brand-dot"></span>Vantrell OBGYN Partners LLC</div>
    <div class="tagline">...connect the dots (docs!)</div>
  </div>
  <div class="contact">2846 Quillan Avenue Suite 240<br>Tucker, Ga 30091</div>
</section>

<section class="sheet envelope-color envelope-pink" aria-label="Envelope, pink">
  <div class="masthead">
    <div class="brand"><span class="brand-dot"></span>Vantrell OBGYN Partners LLC</div>
    <div class="tagline">...connect the dots (docs!)</div>
  </div>
  <div class="contact">2846 Quillan Avenue Suite 240<br>Tucker, Ga 30091</div>
</section>

</body>
</html>
```